Furniture Design Website Homepage

Brief as attached- Homepage Design

Silver Heron Furniture is a national retail emporium offering high quality, unique Scandinavian furniture, lighting and accessories. We are the market leader in this space and currently have 2 Showrooms – Melbourne & Sydney.

Most recently our business model has evolved from purely importing premium, one off vintage pieces to a more scalable model of representing brands and manufacturers exclusively out of Scandinavia. These partners manufacture today which ensures us of supply & quality.

We have now started to engage scandinavian designers and/or their families to re-introduce designs that have long gone out of production. These items are put back into production under the silver heron brand, and we own the world wide rights to them.

Please ensure you use the brief files attached and the catalogue images when creating the design.

Target Market(s)

Silver Heron Furniture - where beautiful Scandinavian design meets my modern Australian life.

We want our target audience to chose Scandinavian for their homes & for us to be their brand of choice.

The current perception is that we offer beautiful design but that it doesn’t suit everyone’s home / life / style.

Also that we are more expensive than most.

Industry/Entity Type

Retail

Requirements
Must have
• The colour scheme should be red and white as per the catalogue I attached. We like the look and feel of this site www.roomfondly.example

The furniture is more luxurious, so we need to target the upper market with a nice sleek look that makes the furniture look expensive.

```html
<!DOCTYPE html>
<html lang="en">
<head>
<meta charset="utf-8">
<title>Silver Heron Furniture – Home</title>
<link href="https://fonts.googleapis.com/css2?family=Arimo:wght@400;700&display=swap" rel="stylesheet">
<style>
:root{
  --red:#c8350f;
  --red-dark:#a82a0a;
  --maroon:#5c0a2a;
  --navy:#1e4f9a;
  --grey-text:#7a7a7a;
  --ink:#222;
  --panel:#f1f1f1;
  --panel-line:#dcdcdc;
  --news-bg:#dcdcdc;
  --footer:#4a4a4a;
  --btn-dark:#2a2a2a;
  --white:#fff;
}
*{box-sizing:border-box;margin:0;padding:0}
html,body{width:962px;height:1200px;overflow:hidden;background:var(--white)}
body{position:relative;font-family:"Arimo",Arial,sans-serif;color:var(--ink);font-size:12px}
.abs{position:absolute}
.top-band{left:0;top:0;width:962px;height:5px;background:var(--red)}
.bottom-band{left:0;top:1183px;width:962px;height:17px;background:var(--red)}

/* brand */
.brand{left:14px;top:60px;display:flex;align-items:center;gap:8px}
.brand-mark{width:22px;height:22px;background:var(--red)}
.brand-name{font-size:34px;font-weight:700;color:#333;letter-spacing:-1px;line-height:1}
.tagline{left:14px;top:120px;font-size:11.5px;font-weight:700;color:#444}

/* cart */
.cart{left:787px;top:32px;width:160px}
.cart-title{display:flex;align-items:center;gap:6px;font-weight:700;font-size:12px;padding-left:2px}
.cart-line{font-weight:700;font-size:11.5px;margin-top:6px;padding-left:13px}
.cart-line span{color:var(--red)}
.cart-btns{display:flex;gap:6px;margin-top:14px;padding-left:10px}
.btn-dark{background:var(--btn-dark);color:var(--white);font-size:11px;font-weight:700;width:72px;height:20px;line-height:20px;text-align:center;box-shadow:2px 2px 2px #aaa}

/* nav */
.nav{left:8px;top:142px;width:954px;height:39px;background:var(--red);border-radius:4px 0 0 4px;display:flex;align-items:center;padding-left:18px}
.nav a{color:var(--white);text-decoration:none;font-weight:700;font-size:12.5px;margin-right:16px}
.nav .soc{width:8px;height:8px;border-radius:50%;background:var(--white);margin-right:18px}
.nav-active{left:52px;top:141px;width:0;height:0;border-left:5px solid transparent;border-right:5px solid transparent;border-top:6px solid #f5d000}
.account{left:824px;top:145px;width:138px;height:34px;background:var(--white);border-radius:4px 0 0 4px;font-weight:700;font-size:12.5px;display:flex;align-items:center;padding-left:9px;gap:10px}

/* sidebar */
.panel{background:var(--panel);border:1px solid var(--panel-line);border-radius:8px}
.search-panel{left:22px;top:195px;width:244px;height:384px}
.ribbon{height:50px;color:var(--white);font-weight:700;font-size:20px;padding:14px 0 0 21px}
.ribbon-red{left:8px;top:219px;width:271px;background:var(--red)}
.ribbon-maroon{left:8px;top:741px;width:271px;background:var(--maroon)}
.fold{width:0;height:0;border-top:11px solid #555}
.fold-l{border-left:13px solid transparent}
.fold-r{border-right:13px solid transparent}
.search-input{left:31px;top:279px;width:133px;height:22px;background:var(--white);border:1px solid #ccc;border-radius:3px}
.btn-red{background:var(--red);color:var(--white);font-weight:700;text-align:center;box-shadow:2px 2px 2px #999}
.search-btn{left:171px;top:280px;width:80px;height:21px;font-size:12px;line-height:21px}
.select{background:var(--white);border:1px solid #7b9ebd;height:18px;position:absolute}
.select::after{content:"";position:absolute;right:1px;top:1px;width:14px;height:14px;background:#c7d7ea;border-radius:2px}
.select span{font-size:13px;padding-left:4px;line-height:16px}
.range{left:35px;top:315px;width:134px}
.cat-title{left:35px;top:348px;color:var(--red);font-weight:700;font-size:12px}
.filter{left:36px;font-weight:700;font-size:11.5px;color:#333}
.filter-sel{left:118px;width:70px}
.find-btn{left:80px;top:536px;width:109px;height:21px;line-height:21px;font-size:12px;border-radius:3px}

.keep h3{color:var(--navy);font-size:14.5px;font-weight:700}
.keep{left:35px;top:595px;width:230px}
.keep p{font-size:11.5px;line-height:14px;margin-top:9px;color:#333}
.news-btn-blue{display:block;margin-top:12px;width:158px;height:20px;line-height:20px;background:var(--navy);color:var(--white);font-weight:700;font-size:11.5px;text-align:center;box-shadow:2px 2px 2px #999}
.keep small{display:block;margin-top:8px;color:var(--navy);font-size:11px;padding-left:3px}

.testi-panel{left:22px;top:715px;width:244px;height:226px}
.quote{left:42px;top:805px;width:186px;color:var(--maroon);font-size:11.5px;line-height:14px;text-align:justify}
.quote p{padding-left:28px}
.qmark{font-family:Georgia,serif;font-size:34px;font-weight:700;color:var(--maroon);position:absolute;line-height:1}

.cards-title{left:35px;top:960px;color:var(--red);font-weight:700;font-size:14.5px}
.card-art{left:40px;top:990px;width:142px;height:88px;border-radius:6px;background:linear-gradient(135deg,#2f6fd0,#174a9a);transform:skewX(-4deg);box-shadow:0 6px 8px #bbb}

/* main */
.welcome{left:303px;top:221px;font-size:34px;font-weight:700;color:var(--grey-text)}
.intro{left:309px;top:264px;width:630px;font-size:11.5px;line-height:13px;color:#333;text-align:justify}
.hero{left:303px;top:313px;width:638px;height:322px;border:2px solid #8a8a8a;background:var(--panel)}
.hero-img{position:absolute;left:0;top:0;width:429px;height:318px;background:linear-gradient(90deg,#f2eeea 0%,#f2eeea 55%,#d9402e 56%,#d9402e 100%)}
.hero-img::after{content:"";position:absolute;left:0;right:0;bottom:0;height:70px;background:linear-gradient(#bfb3a6,#9f958b)}
.hero-list{position:absolute;left:446px;top:23px;width:188px}
.hero-item{height:73px;padding:11px 0 0 16px}
.hero-item.active{background:linear-gradient(#e6e6e6,#8d8d8d);height:53px;margin-bottom:20px;position:relative}
.hero-item.active::before{content:"";position:absolute;left:-10px;top:18px;border-top:6px solid transparent;border-bottom:6px solid transparent;border-right:10px solid #9d9d9d}
.hero-item h4{color:var(--red);font-size:14.5px;font-weight:700}
.hero-item p{font-size:12px;margin-top:4px;padding-left:4px;color:#222}
.hero-item.active p{color:var(--white)}

.collections{left:297px;top:683px;font-size:29px;font-weight:700;color:var(--grey-text)}
.product{position:absolute;top:726px;width:150px}
.product-img{width:149px;height:126px;border:1px solid #333;background:radial-gradient(circle at 50% 50%,#c9342e 0%,#e7e0dc 40%,#fff 70%)}
.product h5{color:var(--red);font-size:12px;font-weight:700;margin-top:9px;padding-left:2px}
.price{font-weight:700;font-size:11.5px;margin-top:4px;padding-left:2px}
.product-btns{display:flex;gap:6px;margin-top:7px}
.product-btns .btn-red{height:19px;line-height:19px;font-size:11px;padding:0 4px}

.newsletter{left:294px;top:952px;width:654px;height:138px;background:var(--news-bg)}
.news-tab{position:absolute;left:0;top:6px;background:var(--white);color:var(--red);font-size:18px;font-weight:700;padding:2px 18px 2px 6px;border-radius:0 4px 4px 0;height:25px}
.news-tab::after{content:"";position:absolute;left:-7px;top:25px;border-top:6px solid #fff;border-left:7px solid transparent}
.news-copy{position:absolute;left:12px;top:36px;font-size:12px;color:#333}
.news-label{position:absolute;font-weight:700;font-size:12px}
.news-field{position:absolute;width:120px;height:21px;background:var(--white);border:1px solid #aaa}
.news-btn-maroon{position:absolute;left:393px;top:72px;width:162px;height:20px;line-height:20px;background:var(--maroon);color:var(--white);font-weight:700;font-size:12px;text-align:center;box-shadow:2px 2px 2px #888}
.news-privacy{position:absolute;left:397px;top:100px;color:var(--red);font-size:11.5px}

.footer{left:69px;top:1120px;width:825px;height:63px;background:var(--footer);border-radius:4px 4px 0 0;color:var(--white);font-size:12px;padding:33px 0 0 10px;word-spacing:1px}
</style>
</head>
<body>
<div class="abs top-band"></div>

<header>
  <div class="abs brand"><span class="brand-mark"></span><span class="brand-name">silver heron</span></div>
  <div class="abs tagline">The Best of Modern And Classic Scandinavian Design</div>

  <div class="abs cart">
    <div class="cart-title">
      <svg width="36" height="16" viewBox="0 0 36 16" aria-hidden="true"><g stroke="#222" stroke-width="1.4" fill="none"><path d="M0 5h10M3 8h8M6 11h6"/><path d="M14 2h3l3 9h10l2-6H18"/></g><circle cx="21" cy="14" r="1.5" fill="#222"/><circle cx="29" cy="14" r="1.5" fill="#222"/></svg>
      Shopping Cart
    </div>
    <div class="cart-line"><span>Items :</span> 0</div>
    <div class="cart-line"><span>Total :</span> $0.00</div>
    <div class="cart-btns"><div class="btn-dark">View Cart</div><div class="btn-dark">Checkout</div></div>
  </div>

  <nav class="abs nav">
    <a>ABOUT US</a><a>FURNITURE RESTORATION</a><a>MEDIA</a><a>FAQ</a><a>MAILING LIST</a><a>BLOG</a><a>SITE SEARCH</a><a>CONTACT US</a>
    <span class="soc"></span><span class="soc"></span>
  </nav>
  <div class="abs nav-active"></div>
  <div class="abs account">ACCOUNT <span>|</span> LOGIN</div>
</header>

<aside>
  <div class="abs panel search-panel"></div>
  <div class="abs ribbon ribbon-red">PRODUCT SEARCH</div>
  <div class="abs fold fold-l" style="left:8px;top:269px"></div>
  <div class="abs fold fold-r" style="left:266px;top:269px"></div>
  <div class="abs search-input"></div>
  <div class="abs btn-red search-btn">SEARCH ⚲</div>
  <div class="select range"><span>Browse Our Range</span></div>
  <div class="abs cat-title">View Products By Category</div>
  <div class="abs filter" style="top:374px">Room :</div><div class="select filter-sel" style="top:373px"></div>
  <div class="abs filter" style="top:404px">Furniture :</div><div class="select filter-sel" style="top:403px"></div>
  <div class="abs filter" style="top:433px">Designers :</div><div class="select filter-sel" style="top:432px"></div>
  <div class="abs filter" style="top:463px">Brands :</div><div class="select filter-sel" style="top:462px"></div>
  <div class="abs filter" style="top:493px">Accessories :</div><div class="select filter-sel" style="top:492px"></div>
  <div class="abs btn-red find-btn">Find Products »</div>

  <div class="abs keep">
    <h3>Keep Up To Date</h3>
    <p>Discover exclusive offers,<br>products previews and much more..</p>
    <span class="news-btn-blue">JOIN OUR NEWS LETTER</span>
    <small>We value your privacy</small>
  </div>

  <div class="abs panel testi-panel"></div>
  <div class="abs ribbon ribbon-maroon">TESTIMONIALS</div>
  <div class="abs fold fold-l" style="left:8px;top:791px"></div>
  <div class="abs fold fold-r" style="left:266px;top:791px"></div>
  <div class="abs quote">
    <span class="qmark" style="left:0;top:-8px">“</span>
    <p>Lorem Ipsum is simply dummy text of the printing and typesetting industry. Lorem Ipsum has been the industry's standard dummy text ever since the 1500s, when an unknown printer .</p>
    <span class="qmark" style="right:-12px;bottom:-20px">”</span>
  </div>

  <div class="abs cards-title">We Accpet Credit Cards</div>
  <div class="abs card-art" role="img" aria-label="Blue payment card artwork"></div>
</aside>

<main>
  <h1 class="abs welcome">Welcome To Silver Heron</h1>
  <p class="abs intro">Lorem Ipsum is simply dummy text of the printing and typesetting industry. Lorem Ipsum has been the industry's standard dummy text ever since the 1500s, when an unknown printer took a galley of type and scrambled it to make a type specimen book.</p>

  <section class="abs hero">
    <div class="hero-img" role="img" aria-label="Red corner sofa with orange ottoman and cushions in a living room with a red patterned wall and pendant lights"></div>
    <div class="hero-list">
      <div class="hero-item active"><h4>Furniture</h4><p>View Collections</p></div>
      <div class="hero-item"><h4>Accessories</h4><p>View Collections</p></div>
      <div class="hero-item"><h4>Lighting</h4><p>View Collections</p></div>
      <div class="hero-item"><h4>Scandinavian Design</h4><p>View Collections</p></div>
    </div>
  </section>

  <h2 class="abs collections">Our Collections</h2>

  <article class="product" style="left:296px">
    <div class="product-img" role="img" aria-label="White ball chair with red interior"></div>
    <h5>Product Name</h5><div class="price">$ 2.299</div>
    <div class="product-btns"><span class="btn-red">More Details</span><span class="btn-red">Add to cart</span></div>
  </article>
  <article class="product" style="left:464px">
    <div class="product-img" role="img" aria-label="Red egg lounge chair"></div>
    <h5>Product Name</h5><div class="price">$ 2.299</div>
    <div class="product-btns"><span class="btn-red">More Details</span><span class="btn-red">Add to cart</span></div>
  </article>
  <article class="product" style="left:632px">
    <div class="product-img" role="img" aria-label="Red tripod floor lamp"></div>
    <h5>Product Name</h5><div class="price">$ 2.299</div>
    <div class="product-btns"><span class="btn-red">More Details</span><span class="btn-red">Add to cart</span></div>
  </article>
  <article class="product" style="left:800px">
    <div class="product-img" style="background:radial-gradient(circle at 50% 50%,#2a2a2a 0%,#d8d8d8 45%,#fff 70%)" role="img" aria-label="Black leather armchair with chrome frame"></div>
    <h5>Product Name</h5><div class="price">$ 2.299</div>
    <div class="product-btns"><span class="btn-red">More Details</span><span class="btn-red">Add to cart</span></div>
  </article>

  <section class="abs newsletter">
    <div class="news-tab">Join Our Newletter</div>
    <p class="news-copy">Discover Eclusive offers, Product Previews, Information on sales and much more</p>
    <span class="news-label" style="left:12px;top:65px">Name</span><span class="news-field" style="left:52px;top:60px"></span>
    <span class="news-label" style="left:12px;top:96px">State</span><span class="select" style="left:53px;top:92px;width:72px"></span>
    <span class="news-label" style="left:190px;top:65px">E-mail</span><span class="news-field" style="left:251px;top:60px"></span>
    <span class="news-label" style="left:190px;top:96px">Postcode</span><span class="news-field" style="left:251px;top:90px"></span>
    <span class="news-btn-maroon">JOIN OUR NEWS LETTER</span>
    <span class="news-privacy">We value your privacy</span>
  </section>
</main>

<footer class="abs footer">ABOUT US &nbsp;|&nbsp; FURNITURE RESTORATION &nbsp;|&nbsp; MEDIA &nbsp;|&nbsp; FAQ &nbsp;|&nbsp; MAILING LIST &nbsp;|&nbsp; BLOG &nbsp;|&nbsp; SITE SEARCH &nbsp;|&nbsp; CONTACT US</footer>
<div class="abs bottom-band"></div>
</body>
</html>
```